Occupational Therapy Clinic Advertisement

Create an advertisement for a magazine. Below I have attached my original ad (Ad 2020.pdf) . I want the ad changed and it should be eye catching. I would like a eye catching graphics added in the ad. It should be a graphic image that applies to education. I am attaching a sample graphic image of that I liked from someone elses ad- it should not be the same- it just is there to show what I like. Please use the same words from my original ad.Dimensions: 3.75in x 10.3 in

Target Market(s)

Parents of School aged children

Requirements
Must have
• Must have eye catching Graphic. Colors should be eye catching for a typed magazine.

```html
<!DOCTYPE html>
<html lang="en">
<head>
<meta charset="utf-8">
<title>Bright Steps OT Services – Advertisement</title>
<link href="https://fonts.googleapis.com/css2?family=Alfa+Slab+One&family=Montserrat:wght@400;700&family=Teko:wght@600;700&display=swap" rel="stylesheet">
<style>
  :root{
    --blue:#0094d4;
    --sky:#3aa9dd;
    --pink:#d83f8d;
    --pink-light:#ec7fb6;
    --magenta:#cc1166;
    --navy:#1b1a6e;
    --yellow:#fff03a;
    --amber:#f5c22c;
    --paper:#ffffff;
    --doodle:#f3f3f5;
  }
  *{margin:0;padding:0;box-sizing:border-box}
  html,body{width:1200px;height:2810px;overflow:hidden;background:var(--paper)}
  .ad{position:relative;width:1200px;height:2810px;overflow:hidden;background:var(--paper);font-family:"Montserrat",Arial,sans-serif;color:var(--navy)}
  .shapes{position:absolute;inset:0}
  .txt{position:absolute;white-space:nowrap;line-height:1}
  .brand-name{left:34px;top:58px;font-family:"Alfa Slab One",Georgia,serif;font-size:138px;color:var(--paper);line-height:126px;letter-spacing:1px}
  .brand-sub{left:38px;top:326px;font-family:"Teko",Arial,sans-serif;font-weight:700;font-size:84px;color:var(--paper);line-height:64px;letter-spacing:1px}
  .questions{right:38px;top:684px;text-align:right;font-weight:700;font-size:41px;line-height:55px}
  .questions .accent{color:var(--magenta)}
  .questions .rule{height:0;border-top:6px dotted var(--navy);width:590px;margin:22px 0 24px auto}
  .headline{left:0;width:1186px;top:1092px;text-align:center;font-family:"Alfa Slab One",Georgia,serif;font-size:120px;line-height:119px;color:var(--navy);letter-spacing:1px}
  .headline .struck{position:relative;display:inline-block}
  .headline .struck::after{content:"";position:absolute;left:-26px;right:-26px;top:54%;height:12px;background:var(--magenta)}
  .tag{display:inline-block;font-weight:700;padding:4px 6px 2px;line-height:1}
  .tag.yellow{background:var(--yellow)}
  .tag.pink{background:var(--pink)}
  .tag.blue{background:var(--sky)}
  .evaluate{left:25px;top:1875px;font-size:40px;line-height:55px}
  .treat{right:38px;top:1875px;font-size:40px;line-height:55px;text-align:right}
  .treat-note{right:38px;top:2048px;font-size:43px;line-height:60px;text-align:right;font-weight:700}
  .ages{margin-top:24px}
  .board{left:211px;top:2350px;font-weight:700;font-size:34px;line-height:47px;color:var(--navy)}
  .contact{left:50px;width:310px;top:2635px;text-align:center;font-weight:700;font-size:31px;line-height:43px;color:var(--navy)}
  .location{right:38px;top:2410px;text-align:right;color:var(--paper);font-size:38px;line-height:51px}
  .location b{font-weight:700}
</style>
</head>
<body>
<div class="ad">
  <svg class="shapes" width="1200" height="2810" viewBox="0 0 1200 2810">
    <defs>
      <radialGradient id="idea-glow" cx="50%" cy="45%" r="50%">
        <stop offset="0%" stop-color="var(--pink-light)"/>
        <stop offset="100%" stop-color="var(--pink)"/>
      </radialGradient>
      <clipPath id="pink-area"><circle cx="892" cy="2669" r="445"/></clipPath>
    </defs>
    <rect role="img" aria-label="Faint line doodles of school supplies: globes, rulers, paper planes, palettes and glasses" x="0" y="0" width="1200" height="2810" fill="var(--doodle)" opacity="0.45"/>
    <circle cx="200" cy="-100" r="630" fill="var(--blue)"/>
    <g style="mix-blend-mode:multiply">
      <circle cx="668" cy="477" r="160" fill="var(--pink)"/>
      <path d="M760 600 L801 650 L715 620 Z" fill="var(--pink)"/>
    </g>
    <circle cx="668" cy="470" r="112" fill="url(#idea-glow)" role="img" aria-label="Line illustration of a glowing light bulb, the idea symbol"/>
    <polygon points="145,582 214,622 214,702 145,742 76,702 76,622" fill="none" stroke="var(--magenta)" stroke-width="10"/>
    <rect x="972" y="174" width="106" height="86" fill="none" stroke="var(--yellow)" stroke-width="9"/>
    <polygon points="1047,416 1131,416 1089,474" fill="none" stroke="var(--blue)" stroke-width="6"/>
    <polygon points="437,800 492,852 437,904 382,852" fill="none" stroke="var(--yellow)" stroke-width="7"/>
    <polygon points="185,1018 225,1080 145,1080" fill="none" stroke="var(--blue)" stroke-width="6"/>
    <polygon points="1048,1404 1108,1464 1048,1524 988,1464" fill="none" stroke="var(--magenta)" stroke-width="7"/>
    <polygon points="638,1876 686,1902 686,1952 638,1978 590,1952 590,1902" fill="none" stroke="var(--yellow)" stroke-width="7"/>
    <circle cx="892" cy="2669" r="445" fill="var(--pink)"/>
    <circle cx="223" cy="2725" r="215" fill="var(--yellow)"/>
    <circle cx="223" cy="2725" r="215" fill="var(--amber)" clip-path="url(#pink-area)"/>
    <g style="mix-blend-mode:multiply">
      <circle cx="327" cy="2420" r="155" fill="var(--sky)"/>
      <path d="M200 2340 L85 2332 L185 2420 Z" fill="var(--sky)"/>
    </g>
  </svg>

  <div class="txt brand-name">BRIGHT<br>STEPS</div>
  <div class="txt brand-sub">OT SERVICES<br>(555) 014-2288</div>

  <div class="txt questions">
    <p>Does your child struggle<br>with Reading/Kriah?</p>
    <div class="rule"></div>
    <p class="accent">Knows the information<br>but fails the test?</p>
    <div class="rule"></div>
    <p>Has difficulty remembering<br>names and dates?</p>
  </div>

  <div class="txt headline">YES<br>YOUR CHILD<br><span class="struck">CAN</span><br>WILL<br>SUCCEED<br>IN SCHOOL!</div>

  <div class="txt evaluate">
    <span class="tag yellow">We Evaluate:</span><br>
    Using standardized<br>Evaluations
    <div class="ages"><span class="tag pink">Ages:</span><br>6-18</div>
  </div>

  <div class="txt treat">
    <span class="tag blue">We Treat:</span><br>
    Using Researched<br>based techniques
  </div>
  <div class="txt treat-note">We Treat the underlying<br>processing deficits</div>

  <div class="txt board">Board of<br>Ed OT RSA's<br>Accepted</div>

  <div class="txt contact">Dana Morel<br>OTR/L<br>(555) 014-2288</div>

  <div class="txt location">
    <b>Located in Borough Park<br>Evaluations done in<br>Borough Park &amp; Staten Island</b><br>
    For more information or to be<br>added to our email list,<br>please email to:<br>
    <b>hello@brightstepsot.example</b>
  </div>
</div>
</body>
</html>
```